Mortgage Loan officer needs clean/modern business card design

Looking for a clean, modern 2-sided business card design. We like the earth tones used in our logo and website http://varnhill-lending.com . Would also like to incorporate: 1) Something special to make our card stand out - a pop of color or embossed logo, for instance and 2) please include "Mortgage Loans" "Reverse Mortgages" "Private Money Loans" on back of card with the logo.

Front: Needs to include agent/company license info - see website. Agent name: Marco Lindqvist

Here are fonts and colors used for our logo:
Font: Avenir Next
Colors:
#2c3539 - Dark Gray
#576870 - Light Gray
#ffffff - Background White

Target Market(s)

Prospects and current clients. Will also be distributing to people in professional network (attorneys and CPAs)

Industry/Entity Type

Business

Contact Information for Business Card

Include agent name, contact info, website on front, licensing info for agent an company. Logo and services offered on back

Font styles to use
Other font styles liked:
• Avenir Next

Requirements
Must have
• See project description
Should not have
• Nothing cheesy

```html
<!DOCTYPE html>
<html lang="en">
<head>
<meta charset="utf-8">
<title>Varnhill Lending – Business Card</title>
<link rel="stylesheet" href="https://fonts.googleapis.com/css2?family=Nunito+Sans:wght@400;600;700&display=swap">
<style>
  :root {
    --dark-gray: #2c3539;
    --card-dark: #353c40;
    --light-gray: #576870;
    --band-gray: #8a9093;
    --band-text: #394044;
    --muted-text: #9aa0a3;
    --ring-muted: #8d9497;
    --white: #ffffff;
    --paper: #f6f6f6;
    --stage: #e4e4e4;
    --font-main: "Nunito Sans", "Avenir Next", Arial, sans-serif;
  }
  * { margin: 0; padding: 0; box-sizing: border-box; }
  html, body { width: 1200px; height: 576px; overflow: hidden; }
  body {
    position: relative;
    background: var(--stage);
    font-family: var(--font-main);
  }
  .card {
    position: absolute;
    top: 138px;
    width: 484px;
    height: 294px;
    border-radius: 14px;
    overflow: hidden;
    background: var(--card-dark);
  }
  .card--back { left: 82px; }
  .card--front { left: 602px; }

  .brand-ring {
    position: absolute;
    width: 164px;
    height: 164px;
    border-radius: 50%;
    border: 1.5px solid var(--ring-muted);
    display: flex;
    align-items: center;
    justify-content: center;
    text-align: center;
  }
  .brand-name {
    font-size: 18px;
    font-weight: 400;
    line-height: 1.2;
  }

  /* Back side */
  .card--back .brand-ring { left: 160px; top: 50px; }
  .card--back .brand-name { color: var(--muted-text); }
  .services-band {
    position: absolute;
    left: 0;
    top: 250px;
    width: 100%;
    height: 24px;
    background: var(--band-gray);
    color: var(--band-text);
    font-size: 12.5px;
    line-height: 24px;
    text-align: center;
    letter-spacing: 0.1px;
  }
  .services-band .divider { margin: 0 6px; }

  /* Front side */
  .front-shape { position: absolute; inset: 0; }
  .agent {
    position: absolute;
    left: 24px;
    top: 26px;
    color: var(--white);
  }
  .agent-name { font-size: 19px; font-weight: 700; line-height: 1.1; }
  .agent-title { font-size: 9.5px; color: #d6d9db; margin-top: 3px; }
  .contact-list {
    position: absolute;
    left: 24px;
    top: 158px;
    list-style: none;
    color: #e9ebec;
    font-size: 11.5px;
  }
  .contact-list li {
    display: flex;
    align-items: center;
    height: 18px;
  }
  .contact-list svg { width: 11px; height: 11px; margin-right: 12px; fill: none; stroke: #e9ebec; stroke-width: 1.3; }
  .contact-list .address { margin-top: 2px; }
  .license-band {
    position: absolute;
    left: 0;
    top: 247px;
    width: 290px;
    height: 23px;
    background: var(--light-gray);
    color: var(--white);
    font-size: 11.5px;
    line-height: 23px;
    padding-left: 24px;
  }
  .card--front .brand-ring {
    left: 287px;
    top: 64px;
    border-color: var(--dark-gray);
  }
  .card--front .brand-name { color: var(--light-gray); }
</style>
</head>
<body>

  <section class="card card--back" aria-label="Card back">
    <div class="brand-ring">
      <p class="brand-name">Varnhill<br>Lending</p>
    </div>
    <div class="services-band">
      Mortgage Loans<span class="divider">|</span>Reverse Mortgages<span class="divider">|</span>Private Money Loans
    </div>
  </section>

  <section class="card card--front" aria-label="Card front">
    <svg class="front-shape" viewBox="0 0 484 294" width="484" height="294" aria-hidden="true">
      <path d="M290 0 L306 0 Q176 120 252 240 Q158 112 290 0 Z" fill="var(--light-gray)"/>
      <path d="M312 0 Q180 148 294 294" fill="none" stroke="var(--white)" stroke-width="3"/>
      <path d="M318 0 Q186 148 296 294 L484 294 L484 0 Z" fill="var(--paper)"/>
    </svg>

    <div class="agent">
      <p class="agent-name">Marco Lindqvist</p>
      <p class="agent-title">Owner/Director</p>
    </div>

    <ul class="contact-list">
      <li>
        <svg viewBox="0 0 12 12"><path d="M2 4 Q6 1 10 4 L9 5.5 L7.5 4.5 L4.5 4.5 L3 5.5 Z M3 6 L9 6 L10 10 L2 10 Z" fill="#e9ebec" stroke="none"/></svg>
        0412 587 309
      </li>
      <li>
        <svg viewBox="0 0 12 12"><circle cx="6" cy="6" r="5"/><ellipse cx="6" cy="6" rx="2.2" ry="5"/><path d="M1 6 H11 M2 3.5 H10 M2 8.5 H10"/></svg>
        www.varnhill-lending.com
      </li>
      <li>
        <svg viewBox="0 0 12 12"><rect x="1" y="2.5" width="10" height="7"/><path d="M1 2.5 L6 6.5 L11 2.5"/></svg>
        marco@varnhill-lending.com
      </li>
      <li class="address">58 Harlow Lane, Brookvale NSW 2100</li>
    </ul>

    <div class="license-band">License No.: 12345678</div>

    <div class="brand-ring">
      <p class="brand-name">Varnhill<br>Lending</p>
    </div>
  </section>

</body>
</html>
```